Political Candidate Newspaper Advertisement

I would like a newspaper ad for my campaign for election to City Council. The banner ad is 10 cm high x 26.2 cm wide. The banner will contain a photo and the following text (or words to similar effect):
VOTE
DENNIS HALE
COMO BEACH
For a
SAFE
CARING
CONNECTED
COMMUNITY
Lifetime commitment to local clubs, charities and international aid
Local business owner
Founder of Open-Gate Week
Councillor, Mediator, B.Sc., MBA
The Councillor you know and can call for help
Respects our heritage and our future
Listens to the wisdom and needs of older residents
Promotes more young people
Protects our South Perth environment
Authorised by Dennis Hale 5/348 Kelby Rd, Como. 9317 2864
I use MS Publisher and PhotoShop so I'd like the product to be in a form I can use. After ther banner ad is done, and if it is good, I wish to pay the designer to use the same theme to produce another newspaper ad, a brochure and a poster.
My simple version is attached. A photo is also attached.
I'm hoping you do better.
18-80 years old
Business
- simple fonts
- A TICK somewhere around the word Vote would be good.
Mention of www.fairlandward.notepage.net if possible, perhaps at the bottom of the page, along with the Authorised by ... text.

```html
<!DOCTYPE html>
<html lang="en">
<head>
<meta charset="utf-8">
<title>Vote Dennis Hale – Como Beach</title>
<link rel="stylesheet" href="https://fonts.googleapis.com/css2?family=Source+Sans+3:wght@400;600;700;800&display=swap">
<style>
  :root {
    --sky-light: #2bb4ef;
    --sky: #0a9ae0;
    --sky-deep: #0786cf;
    --navy-bar: #0b4d9e;
    --band: #0b5fb4;
    --band-dark: #0a4f9c;
    --yellow: #f5ec1c;
    --white: #ffffff;
    --tick-box: #7fc0ea;
    --tick-edge: #1c6fb8;
    --tick: #2b2d8a;
    --photo-light: #f4f5f7;
    --photo-mid: #d9dbe0;
  }
  * { margin: 0; padding: 0; box-sizing: border-box; }
  html, body { width: 1200px; height: 457px; overflow: hidden; background: var(--white); }
  body { font-family: "Source Sans 3", "Myriad Pro", Arial, sans-serif; }

  .banner { position: relative; width: 1200px; height: 457px; overflow: hidden; }
  .banner-bg { position: absolute; inset: 0; }

  .headline-vote {
    position: absolute; left: 46px; top: 22px;
    font-size: 70px; font-weight: 800; line-height: 1;
    color: var(--yellow); letter-spacing: -0.5px;
  }
  .tick-box { position: absolute; left: 230px; top: 33px; width: 98px; height: 98px; }

  .candidate-name {
    position: absolute; left: 337px; top: 30px;
    font-size: 79px; font-weight: 700; line-height: 1;
    color: var(--white); letter-spacing: -0.5px;
  }
  .ward-name {
    position: absolute; left: 340px; top: 100px;
    font-size: 37px; font-weight: 400; line-height: 1;
    color: var(--white);
  }

  .slogan-bar {
    position: absolute; left: 47px; top: 148px; width: 674px; height: 40px;
    background: var(--navy-bar); border: 1px solid var(--yellow);
    color: var(--white); font-weight: 700;
    display: flex; align-items: center; justify-content: center;
    font-size: 26px; letter-spacing: 0.3px;
    box-shadow: 0 6px 8px rgba(0, 40, 100, 0.35);
  }
  .slogan-bar .small { font-size: 20px; }
  .slogan-bar .dot { font-size: 18px; margin: 0 9px; }

  .credentials, .promises {
    position: absolute; list-style: none;
    color: var(--white); font-size: 17.5px; line-height: 29px; font-weight: 400;
  }
  .credentials { left: 47px; top: 218px; width: 320px; }
  .credentials .wrap { line-height: 23px; padding-bottom: 6px; }
  .promises { left: 408px; top: 217px; }

  .footer-url, .footer-auth {
    position: absolute; top: 422px;
    font-size: 17.5px; color: var(--yellow); line-height: 1;
  }
  .footer-url { left: 47px; font-weight: 700; }
  .footer-auth { left: 410px; font-weight: 400; }
</style>
</head>
<body>
<div class="banner">
  <svg class="banner-bg" width="1200" height="457" viewBox="0 0 1200 457">
    <defs>
      <linearGradient id="skyFill" x1="0" y1="0" x2="0" y2="1">
        <stop offset="0" stop-color="var(--sky-light)"/>
        <stop offset="0.5" stop-color="var(--sky)"/>
        <stop offset="1" stop-color="var(--sky-deep)"/>
      </linearGradient>
      <linearGradient id="bandFill" x1="0" y1="0" x2="0" y2="1">
        <stop offset="0" stop-color="var(--band)"/>
        <stop offset="1" stop-color="var(--band-dark)"/>
      </linearGradient>
      <linearGradient id="portraitFill" x1="0" y1="0" x2="0" y2="1">
        <stop offset="0" stop-color="var(--photo-light)"/>
        <stop offset="1" stop-color="var(--photo-mid)"/>
      </linearGradient>
    </defs>
    <rect width="1200" height="457" fill="url(#skyFill)"/>
    <rect y="412" width="1200" height="45" fill="url(#bandFill)"/>
    <path d="M870,0 C835,45 812,95 830,118 C860,150 905,230 908,457" fill="none" stroke="var(--band-dark)" stroke-width="6"/>
    <g role="img" aria-label="Portrait photo of candidate Dennis Hale in suit and tie, smiling, on a white background">
      <path d="M878,0 C845,45 822,95 840,118 C872,152 912,230 914,457 L1200,457 L1200,0 Z" fill="url(#portraitFill)"/>
    </g>
    <path d="M878,0 C845,45 822,95 840,118 C872,152 912,230 914,457" fill="none" stroke="var(--white)" stroke-width="2"/>
  </svg>

  <div class="headline-vote">VOTE</div>
  <svg class="tick-box" viewBox="0 0 98 98" aria-hidden="true">
    <rect x="1.5" y="1.5" width="95" height="95" rx="12" fill="var(--tick-box)" stroke="var(--tick-edge)" stroke-width="3"/>
    <path d="M18,52 C24,55 30,62 36,74 C46,50 62,28 84,16 C64,32 50,52 38,84 C33,70 26,60 18,52 Z" fill="var(--tick)"/>
  </svg>
  <div class="candidate-name">DENNIS HALE</div>
  <div class="ward-name">COMO BEACH</div>

  <div class="slogan-bar">
    For a&nbsp;S<span class="small">AFE</span><span class="dot">•</span>C<span class="small">ARING</span><span class="dot">•</span>C<span class="small">ONNECTED</span><span class="dot">•</span>C<span class="small">OMMUNITY</span>
  </div>

  <ul class="credentials">
    <li class="wrap">Lifetime commitment to local clubs, charities and international aid</li>
    <li>Local business owner</li>
    <li>Founder of Open-Gate Week</li>
    <li>Councillor, Mediator, B.Sc., MBA</li>
  </ul>

  <ul class="promises">
    <li>The Councillor you know and can call for help</li>
    <li>Respects our heritage and our future</li>
    <li>Listens to the wisdom and needs of older residents</li>
    <li>Promotes more young people</li>
    <li>Protects our South Perth environment</li>
  </ul>

  <div class="footer-url">www.fairlandward.notepage.net</div>
  <div class="footer-auth">Authorised by Dennis Hale 5/348 Kelby Rd, Como. 9317 2864</div>
</div>
</body>
</html>
```